Retro Label for old fashioned soda

We need a label for soda we are having private labeled for our retro, 1950's ice cream shop www.maplewhirlcones.com I don't want the label to look like something from 2017 with a retro feel, but more like an original (possibly kinda cheesy) label you'd see from the 1950's with some of the old catch lines like "tastes great", "invigorating" or "it is refreshing!" The prominent brand should be the name of our ice cream shop, The Maple Whirl. the soda is also pure cane sugar so it might be good to have that on somewhere

Label size is 2.4" wide by 4" tall. Here is an example of some retro labels from findoramap. I attached on file to this contest but there are more here: https://www.findoramap.net/search?q=retro+soda+label

The label will be the same for all the flavors with the exception of the flavor name changing somewhere on the label. These are the flavors

Root Beer
Orange
Black Cherry
Lemonade
Raspberry Lime -Rickey
White Birch Beer
Lemon Iced Tea
Vanilla Cream
Orange Cream
Sarsaparilla
Ginger Ale

Industry/Entity Type

Shop

Colors

Designer to choose colors to be used in the design.

Requirements
Must have
• retro feel. authentic old fashioned look

```html
<!DOCTYPE html>
<html lang="en">
<head>
<meta charset="utf-8">
<title>The Maple Whirl — Orange Soda Label</title>
<link rel="stylesheet" href="https://fonts.googleapis.com/css2?family=Alfa+Slab+One&family=Bebas+Neue&family=Oswald:wght@500&display=swap">
<style>
  :root {
    --cream: #f1ecdc;
    --cream-deep: #e6dfca;
    --navy: #1d3049;
    --red: #e04e32;
    --red-dark: #b83a22;
  }
  html, body {
    margin: 0;
    padding: 0;
    width: 720px;
    height: 1200px;
    overflow: hidden;
    background: var(--cream);
  }
  .label {
    position: relative;
    width: 720px;
    height: 1200px;
    box-sizing: border-box;
    border: 14px solid var(--red);
    background: var(--cream);
    overflow: hidden;
  }
  .label-art {
    position: absolute;
    inset: -14px;
    width: 720px;
    height: 1200px;
  }
  .scrollwork {
    position: absolute;
    left: 36px;
    top: 84px;
    width: 620px;
    height: 1000px;
    border-radius: 46% 46% 40% 40%;
    background: radial-gradient(ellipse at center, var(--cream) 35%, var(--cream-deep) 70%, rgba(29,48,73,0.10) 100%);
  }
  .ribbon-text {
    font-family: "Bebas Neue", sans-serif;
    fill: var(--cream);
    letter-spacing: 3px;
  }
  .plaque-text {
    font-family: "Alfa Slab One", serif;
    fill: var(--cream);
    font-size: 40px;
    letter-spacing: 1px;
  }
  .seal-text {
    font-family: "Bebas Neue", sans-serif;
    fill: var(--navy);
    font-size: 40px;
    letter-spacing: 1px;
  }
  .brand-name {
    font-family: "Bebas Neue", sans-serif;
    fill: var(--navy);
    font-size: 92px;
    letter-spacing: 4px;
  }
  .flavor-name {
    font-family: "Oswald", sans-serif;
    font-weight: 500;
    fill: var(--navy);
    font-size: 78px;
    letter-spacing: 2px;
  }
  .ingredients {
    font-family: "Bebas Neue", sans-serif;
    fill: var(--navy);
    font-size: 19px;
    letter-spacing: 0.6px;
  }
</style>
</head>
<body>
<main class="label">
  <div class="scrollwork" role="img" aria-label="Victorian scrollwork and leaf ornament framing the label"></div>

  <svg class="label-art" viewBox="0 0 720 1200" xmlns="http://www.w3.org/2000/svg">
    <defs>
      <path id="top-ribbon-line" d="M150,262 Q360,168 570,262"/>
      <path id="bottom-ribbon-line" d="M205,944 Q375,1012 545,944"/>
    </defs>

    <!-- top slogan ribbon -->
    <g class="slogan-ribbon">
      <path d="M108,262 L140,238 L140,282 Z" fill="var(--red-dark)"/>
      <path d="M612,262 L580,238 L580,282 Z" fill="var(--red-dark)"/>
      <path d="M140,236 Q360,140 580,236 L580,282 Q360,186 140,282 Z" fill="var(--red)"/>
      <text class="ribbon-text" font-size="38" text-anchor="middle">
        <textPath href="#top-ribbon-line" startOffset="50%">IT'S REFRESHING!</textPath>
      </text>
    </g>

    <!-- since plaque -->
    <g class="since-plaque">
      <rect x="228" y="285" width="264" height="70" rx="8" fill="var(--navy)"/>
      <rect x="236" y="293" width="248" height="54" rx="5" fill="none" stroke="var(--cream)" stroke-width="2"/>
      <text class="plaque-text" x="360" y="336" text-anchor="middle">SINCE 1950</text>
    </g>

    <!-- tastes great seal -->
    <g class="seal">
      <circle cx="186" cy="497" r="96" fill="var(--cream)" stroke="var(--navy)" stroke-width="5"/>
      <circle cx="186" cy="497" r="86" fill="none" stroke="var(--navy)" stroke-width="10" stroke-dasharray="3 3"/>
      <circle cx="186" cy="497" r="74" fill="var(--cream)" stroke="var(--navy)" stroke-width="3"/>
      <circle cx="186" cy="497" r="68" fill="none" stroke="#8c94a3" stroke-width="2"/>
      <text class="seal-text" x="186" y="492" text-anchor="middle">TASTES</text>
      <text class="seal-text" x="186" y="532" text-anchor="middle">GREAT!</text>
    </g>

    <!-- diagonal brand banner -->
    <g class="brand-banner" transform="rotate(-43 360 600)">
      <rect x="10" y="538" width="700" height="124" fill="var(--cream)" stroke="var(--navy)" stroke-width="4"/>
      <rect x="20" y="546" width="680" height="108" fill="none" stroke="var(--navy)" stroke-width="1.5"/>
      <path d="M710,538 L760,520 L760,644 L710,662 Z" fill="var(--cream-deep)" stroke="var(--navy)" stroke-width="4"/>
      <text class="brand-name" x="360" y="634" text-anchor="middle">THE MAPLE WHIRL</text>
    </g>

    <!-- flavour -->
    <g class="flavor">
      <text class="flavor-name" x="527" y="706" text-anchor="middle">ORANGE</text>
      <line x1="428" y1="722" x2="626" y2="722" stroke="var(--navy)" stroke-width="2"/>
      <circle cx="420" cy="722" r="3" fill="var(--navy)"/>
      <circle cx="634" cy="722" r="3" fill="var(--navy)"/>
      <text class="flavor-name" x="527" y="794" text-anchor="middle">SODA</text>
    </g>

    <!-- net contents ribbon -->
    <g class="contents-ribbon">
      <path d="M160,930 L188,914 L188,956 Z" fill="var(--red-dark)"/>
      <path d="M590,930 L562,914 L562,956 Z" fill="var(--red-dark)"/>
      <path d="M188,910 Q375,990 562,910 L562,956 Q375,1036 188,956 Z" fill="var(--red)"/>
      <text class="ribbon-text" font-size="27" letter-spacing="1.5" text-anchor="middle">
        <textPath href="#bottom-ribbon-line" startOffset="50%">NET CONTENTS 2 FL OZ . OR OVER</textPath>
      </text>
    </g>

    <text class="ingredients" x="360" y="1168" text-anchor="middle">MADE FROM PURE CANE SUGAR, CITRIC ACID, CARBONATED WATER, HARMLESS COLOR AND FLAVOUR</text>
  </svg>
</main>
</body>
</html>
```